International Trading Company, 'KIRO' needs a Business Card

The company name is "KIRO" and it has own logo design.
I'd like to use its logo on this business card.
I need two side Business Card.
I'll look forward to your great design.
Thank you very much in advance.

Contact Information for Business Card

Company Name : Kiro Harbour Limited
Information Example
Dorian Pallister
Mobile(use icon please) : 1 (212) 555-0143
Tel(use icon please) : 1 (212) 555-0178
Email(use icon please) : dorian27@kiroharbour-mail.com
Address(use icon please) : 482 Halden Ave, New York, NY 10160, USA

```html
<!DOCTYPE html>
<html lang="en">
<head>
<meta charset="utf-8">
<title>Kiro Harbour Limited – Business Card</title>
<link href="https://fonts.googleapis.com/css2?family=Poppins:wght@400;600;700&family=Work+Sans:wght@400&display=swap" rel="stylesheet">
<style>
  :root {
    --backdrop: #e4e4e4;
    --card: #ffffff;
    --ink: #555555;
    --ink-soft: #5a5a5a;
  }
  * { margin: 0; padding: 0; box-sizing: border-box; }
  html, body {
    width: 1200px;
    height: 1000px;
    overflow: hidden;
    background: var(--backdrop);
  }
  .canvas {
    position: relative;
    width: 1200px;
    height: 1000px;
  }
  .card {
    position: absolute;
    left: 248px;
    width: 681px;
    height: 388px;
    background: var(--card);
  }
  .card--front { top: 93px; }
  .card--back { top: 520px; }

  .identity {
    position: absolute;
    left: 78px;
    top: 101px;
    padding-left: 36px;
    border-left: 3px solid var(--ink);
    height: 62px;
  }
  .identity__name {
    font-family: "Poppins", sans-serif;
    font-weight: 600;
    font-size: 19px;
    line-height: 23px;
    letter-spacing: 0.3px;
    color: var(--ink);
    text-transform: uppercase;
    margin-top: -4px;
  }
  .identity__role {
    font-family: "Poppins", sans-serif;
    font-weight: 400;
    font-size: 15px;
    line-height: 22px;
    color: var(--ink);
  }

  .address {
    position: absolute;
    left: 469px;
    top: 96px;
    font-family: "Work Sans", sans-serif;
    font-style: normal;
    font-size: 15.5px;
    line-height: 22px;
    letter-spacing: 0.6px;
    color: var(--ink-soft);
  }

  .contact-line {
    position: absolute;
    left: 77px;
    top: 311px;
    font-family: "Work Sans", sans-serif;
    font-size: 14.5px;
    letter-spacing: 0.55px;
    color: var(--ink-soft);
    white-space: nowrap;
  }

  .brand-name {
    position: absolute;
    left: 0;
    right: 0;
    top: 148px;
    text-align: center;
    font-family: "Poppins", sans-serif;
    font-weight: 700;
    font-size: 84px;
    line-height: 84px;
    letter-spacing: 2px;
    color: var(--ink);
  }
</style>
</head>
<body>
  <main class="canvas">
    <section class="card card--front" aria-label="Business card front">
      <div class="identity">
        <p class="identity__name">Dorian<br>Pallister</p>
        <p class="identity__role">Founder</p>
      </div>
      <address class="address">
        482 Halden Ave,<br>
        New York,<br>
        NY 10160, USA
      </address>
      <p class="contact-line">1 (212) 555-0143 | 1 (212) 555-0178 | dorian27@kiroharbour-mail.com</p>
    </section>

    <section class="card card--back" aria-label="Business card back">
      <p class="brand-name">KIRO</p>
    </section>
  </main>
</body>
</html>
```